Banner Ad for Resume Services Website

The add is for this web site: www.BrightFolioDesk.com

The site offers 4 different services:

- Resume Writing (by a Certified Professional Resume Writer)
- Resume Posting (posts your resume to 85 job sites)
- Resume Distribution (sends your resume to hundreds of recruiters)
- Resume Online website (created an online resume with a domain name to your name)

Colors to be used are Blue, Yellow, etc... please check the website for inspiration.

Check the web site to learn more.

Target Market(s)

Unemployed, Professionals who want to switch jobs, etc..

Industry/Entity Type

Learn

Requirements
Must have
• We definitely one this to be included on the banner:

"Free Resume Samples"

in order to attract clicks.
Nice to have
• Some of the words we suggest to include on the banner are:

"How Good is Your Resume? Ask a Professional !"

Should not have
• No animation !

Do not place the LOGO on the banner as our LOGO might change in the near future. If you already submitted a banner with the LOGO on it, you can replace it with any other graphic that has a Resume/Jobs/BusinessStaff related theme.

```html
<!DOCTYPE html>
<html lang="en">
<head>
<meta charset="utf-8">
<title>BrightFolioDesk – Free Resume Samples</title>
<link rel="stylesheet" href="https://fonts.googleapis.com/css2?family=Arimo:wght@400;700&family=Tinos&display=swap">
<style>
  :root {
    --magenta-deep: #b3139a;
    --magenta: #e0148a;
    --pink: #f0327a;
    --white: #ffffff;
    --ink: #111111;
    --button-dark: #0f3a2c;
    --button-light: #2f6a55;
    --photo-light: #e9e4df;
    --photo-mid: #c9b3a6;
    --photo-warm: #8a5a48;
  }
  * { margin: 0; padding: 0; box-sizing: border-box; }
  html, body { width: 1200px; height: 148px; overflow: hidden; background: var(--white); }
  .banner {
    position: relative;
    width: 1200px;
    height: 148px;
    overflow: hidden;
    background: linear-gradient(90deg, var(--magenta-deep) 0%, var(--magenta) 45%, var(--pink) 70%);
    font-family: "Arimo", Arial, sans-serif;
  }
  .headline {
    position: absolute;
    left: 10px;
    top: 10px;
    color: var(--white);
    font-size: 26px;
    white-space: nowrap;
  }
  .headline .accent { font-size: 40px; }
  .offer {
    position: absolute;
    left: 8px;
    top: 78px;
    color: var(--white);
    font-weight: 700;
    font-size: 48px;
    letter-spacing: -0.5px;
    text-shadow: 2px 2px 2px rgba(0,0,0,0.75);
    white-space: nowrap;
  }
  .cta {
    position: absolute;
    left: 544px;
    top: 94px;
    width: 156px;
    height: 38px;
    border-radius: 19px;
    background: linear-gradient(180deg, var(--button-light) 0%, var(--button-dark) 60%);
    color: var(--white);
    font-family: "Tinos", "Times New Roman", serif;
    font-size: 22px;
    line-height: 38px;
    text-align: center;
    box-shadow: 0 1px 3px rgba(0,0,0,0.5);
  }
  .side-panel { position: absolute; left: 0; top: 0; width: 1200px; height: 148px; }
  .trust {
    position: absolute;
    left: 824px;
    top: 14px;
    color: var(--ink);
    font-weight: 700;
    font-size: 30px;
    line-height: 1.25;
    text-align: center;
  }
  .trust span { display: block; }
  .trust .small { font-size: 26px; }
</style>
</head>
<body>
  <div class="banner">
    <p class="headline">How Good is Your <span class="accent">Resume</span>?Ask a Professional !</p>
    <p class="offer">Free Resume Samples</p>
    <div class="cta">Click Here</div>

    <svg class="side-panel" viewBox="0 0 1200 148" aria-hidden="false">
      <defs>
        <linearGradient id="photoTone" x1="0" y1="0" x2="1" y2="0">
          <stop offset="0" stop-color="var(--photo-light)"/>
          <stop offset="0.6" stop-color="var(--photo-light)"/>
          <stop offset="0.85" stop-color="var(--photo-mid)"/>
          <stop offset="1" stop-color="var(--photo-warm)"/>
        </linearGradient>
      </defs>
      <path d="M750 0 Q770 80 860 148 L1200 148 L1200 0 Z" fill="var(--white)"/>
      <path d="M772 0 Q792 78 880 148 L1200 148 L1200 0 Z" fill="url(#photoTone)"
            role="img" aria-label="Photo of a smiling professional woman holding a pen"/>
      <path d="M760 0 Q780 80 870 148" fill="none" stroke="var(--ink)" stroke-width="3"/>
    </svg>

    <p class="trust"><span>TRUST THE</span><span class="small">PROFESSIONALS</span></p>
  </div>
</body>
</html>
```